Business Card Design for Massage Therapist

*I am a qualified massage therapist & require a business card for my new business 'Tidal Touch & Wellness'.
*Contact details I'd like included on the card are: Elise Brantry, Mobile: 0481562930, Email: tidaltw@mailvane.com
*It is a massage business dedicated to providing quality therapeutic massage treatments, that will later incorporate natural therapies.
* Styles Include: Swedish, Relaxation, Pregnancy, Deep Tissue & Sports Massage
*I offer the styles of massage as listed above & a mobile service that allows clients to book a massage in the comfort of their own home.
*I'd like my logo to be fairly simple, streamlined, modern & reflect what my business services are - one people will easily remember.
*I'd like the colors to represent & emit a sense of calm, be fresh, welcoming, natural colors that appeal to a wide range of people.
*Colors I'd like to see are: pale blue, aqua & greens.

Target Market(s)

Both Male & Female, aged 20 to 65, singles, couples, parents, business people who are interested in their health, fitness & general wellbeing and maintenance. Located in the Harbourvale area and surrounding suburbs of Melbourne.

Industry/Entity Type

Massage

Requirements
Must have
• Fonts used in logos should be owned by the designer.
Should not have
• I don't want the design to have someone being massaged in it (pictures/photos) or have it look too clinical & sterile.

```html
<!DOCTYPE html>
<html lang="en">
<head>
<meta charset="utf-8">
<title>Tidal Touch &amp; Wellness – Business Card</title>
<link rel="stylesheet" href="https://fonts.googleapis.com/css2?family=Roboto:wght@400&display=swap">
<style>
  :root {
    --sky: #b2e9f1;
    --mint: #b3fbd9;
    --mint-pale: #d9fdee;
    --mint-line: #8fe9c4;
    --ink: #111111;
    --paper: #ffffff;
  }
  html, body {
    margin: 0;
    padding: 0;
    width: 1200px;
    height: 848px;
    overflow: hidden;
    background: var(--paper);
  }
  .card {
    position: relative;
    width: 1200px;
    height: 848px;
    overflow: hidden;
    background: var(--paper);
    font-family: "Roboto", Arial, sans-serif;
    color: var(--ink);
  }
  .waves {
    position: absolute;
    inset: 0;
    width: 1200px;
    height: 848px;
  }
  .hands-illustration {
    position: absolute;
    left: 750px;
    top: 40px;
    width: 450px;
    height: 808px;
  }
  .brand-banner {
    position: absolute;
    left: 14px;
    top: 18px;
    width: 719px;
    height: 97px;
    background: var(--sky);
    box-sizing: border-box;
    padding-left: 18px;
    display: flex;
    align-items: center;
  }
  .brand-name {
    margin: 0;
    font-weight: 400;
    font-size: 49px;
    color: var(--paper);
    letter-spacing: 0.2px;
    white-space: nowrap;
  }
  .therapist {
    position: absolute;
    left: 23px;
    top: 240px;
    display: flex;
    align-items: center;
  }
  .therapist-name {
    background: var(--sky);
    color: var(--paper);
    font-size: 33px;
    height: 46px;
    line-height: 48px;
    padding: 0 11px 0 13px;
    white-space: nowrap;
  }
  .therapist-role {
    margin-left: 19px;
    margin-top: 14px;
    font-size: 20px;
    white-space: nowrap;
  }
  .services {
    position: absolute;
    left: 30px;
    top: 342px;
    margin: 0;
    padding: 0;
    list-style: none;
    font-size: 24px;
    line-height: 32px;
  }
  .contact {
    position: absolute;
    left: 14px;
    top: 772px;
    font-size: 28px;
    line-height: 32px;
  }
  .contact p { margin: 0; white-space: nowrap; }
</style>
</head>
<body>
<main class="card">
  <svg class="waves" viewBox="0 0 1200 848" aria-hidden="true">
    <path fill="var(--mint-pale)" d="M0 560 C 20 530, 60 525, 120 532 C 260 550, 400 600, 520 612 C 700 630, 820 520, 920 380 C 980 300, 1080 255, 1200 262 L 1200 848 L 0 848 Z"/>
    <path fill="var(--mint)" d="M0 612 C 10 590, 50 582, 110 588 C 250 602, 400 650, 520 660 C 690 672, 800 560, 900 450 C 990 360, 1080 325, 1200 332 L 1200 848 L 0 848 Z"/>
  </svg>

  <svg class="hands-illustration" viewBox="0 0 450 808" role="img" aria-label="Line illustration of two crossed hands reaching upward">
    <defs>
      <linearGradient id="handsTone" x1="0" y1="0" x2="0" y2="1">
        <stop offset="0" stop-color="#c9f7e6" stop-opacity="0.55"/>
        <stop offset="0.5" stop-color="#a8f2d2" stop-opacity="0.45"/>
        <stop offset="1" stop-color="#9ff0cc" stop-opacity="0.35"/>
      </linearGradient>
    </defs>
    <rect x="0" y="0" width="450" height="808" fill="url(#handsTone)"/>
  </svg>

  <header class="brand-banner">
    <h1 class="brand-name">TIDAL TOUCH &amp; WELLNESS</h1>
  </header>

  <section class="therapist">
    <span class="therapist-name">ELISE BRANTRY</span>
    <span class="therapist-role">MASSAGE THERAPIST</span>
  </section>

  <ul class="services">
    <li>SWEDISH</li>
    <li>RELAXATION</li>
    <li>PREGNANCY</li>
    <li>DEEP TISSUE</li>
    <li>SPORTS MASSAGE</li>
  </ul>

  <address class="contact" style="font-style: normal;">
    <p>MOBILE: 0481 562 930</p>
    <p>E-MAIL: tidaltw@mailvane.com</p>
  </address>
</main>
</body>
</html>
```